Need DL Flyer for Real Estate Drops

We need a real estate flyer ,double sided. With content on 1 side like: Want to know what's your house is worth " contact us today and on other side agent details. We are looking for an ongoing partnership with designer so this assignment will be ongoing

```html
<!DOCTYPE html>
<html lang="en">
<head>
<meta charset="utf-8">
<title>Dunecrest Real Estate DL Flyer</title>
<link href="https://fonts.googleapis.com/css2?family=League+Spartan:wght@600;700;800&family=Montserrat:wght@600&family=Didact+Gothic&display=swap" rel="stylesheet">
<style>
  :root {
    --navy: #0c1632;
    --red: #c92128;
    --white: #ffffff;
    --paper: #f1f1f1;
    --stage: #9d9d9d;
    --ink: #1d1d1f;
  }
  * { box-sizing: border-box; margin: 0; padding: 0; }
  html, body { width: 1142px; height: 1200px; overflow: hidden; }
  body { background: var(--stage); position: relative; font-family: "Didact Gothic", sans-serif; }

  .flyer { position: absolute; top: 111px; height: 920px; box-shadow: 4px 4px 6px rgba(0,0,0,.25); overflow: hidden; background: var(--paper); }
  .flyer--front { left: 112px; width: 430px; }
  .flyer--back { left: 586px; width: 437px; }
  .flyer__art { position: absolute; inset: 0; width: 100%; height: 100%; }

  .brand { position: absolute; top: 44px; left: 0; right: 0; display: flex; align-items: center; justify-content: center; gap: 14px; }
  .brand__mark { width: 34px; height: 34px; background: var(--red); }
  .brand__name { font-family: "Montserrat", sans-serif; font-weight: 600; font-size: 40px; color: var(--white); letter-spacing: -0.5px; }

  .center { position: absolute; left: 0; right: 0; text-align: center; }

  .teaser { top: 574px; left: 40px; right: 160px; font-family: "League Spartan", sans-serif; font-weight: 600; color: var(--red); font-size: 27px; line-height: 29px; }
  .headline { top: 634px; font-family: "League Spartan", sans-serif; font-weight: 800; color: var(--navy); font-size: 51px; line-height: 46px; letter-spacing: -0.5px; }

  .cta { position: absolute; left: 0; right: 0; bottom: 0; height: 121px; background: var(--red); text-align: center; }
  .cta__label { margin-top: 17px; font-family: "League Spartan", sans-serif; font-weight: 600; font-size: 27px; color: var(--white); line-height: 30px; }
  .cta__phone { margin-top: 4px; font-family: "League Spartan", sans-serif; font-weight: 800; font-size: 47px; color: var(--navy); line-height: 50px; letter-spacing: 0.5px; }

  .agent__name { top: 578px; font-family: "League Spartan", sans-serif; font-weight: 700; font-size: 37px; color: var(--red); }
  .agent__role { top: 624px; font-family: "League Spartan", sans-serif; font-weight: 600; font-size: 18px; line-height: 20px; color: var(--navy); }
  .agent__icons { position: absolute; top: 683px; left: 93px; width: 252px; height: 24px; }
  .agent__contact { top: 714px; font-size: 17px; line-height: 22px; color: var(--ink); }

  .side-label { position: absolute; font-family: "Didact Gothic", sans-serif; font-size: 14px; color: var(--ink); letter-spacing: 1px; transform: rotate(-90deg); transform-origin: left top; }
  .side-label--front { left: 84px; top: 1030px; }
  .side-label--back { left: 1040px; top: 1031px; }
  .caption { position: absolute; top: 1092px; left: 0; right: 0; text-align: center; font-family: "Didact Gothic", sans-serif; font-size: 17px; color: var(--ink); letter-spacing: .5px; }
</style>
</head>
<body>

<section class="flyer flyer--front">
  <svg class="flyer__art" viewBox="0 0 430 920" aria-hidden="true">
    <defs>
      <linearGradient id="houseTone" x1="0" y1="0" x2="0" y2="1">
        <stop offset="0" stop-color="#d8dde2"/>
        <stop offset=".55" stop-color="#c9c2b4"/>
        <stop offset=".8" stop-color="#6f7a5a"/>
        <stop offset="1" stop-color="#4d8a34"/>
      </linearGradient>
      <linearGradient id="dealTone" x1="0" y1="0" x2="1" y2="1">
        <stop offset="0" stop-color="#eef1f5"/>
        <stop offset=".6" stop-color="#c9a58a"/>
        <stop offset="1" stop-color="#8a9bb0"/>
      </linearGradient>
    </defs>
    <rect width="430" height="920" fill="var(--navy)"/>
    <polygon points="0,224 217,142 430,224 430,234 217,156 0,234" fill="var(--red)"/>
    <polygon points="0,240 217,168 430,240 430,588 217,522 0,588" fill="url(#houseTone)" role="img" aria-label="Photo of a modern two-storey family house at dusk with lit eaves and a green lawn"/>
    <polygon points="0,586 217,520 430,586 430,600 217,536 0,600" fill="var(--red)"/>
    <polygon points="0,598 217,534 430,598 430,920 0,920" fill="var(--paper)"/>
    <polygon points="349,516 397,543 397,598 349,626 301,598 301,543" fill="var(--white)" stroke="var(--navy)" stroke-width="3"/>
    <polygon points="349,524 390,547 390,594 349,618 308,594 308,547" fill="url(#dealTone)" role="img" aria-label="Photo of a handshake in front of a city skyline"/>
  </svg>

  <div class="brand"><span class="brand__mark"></span><span class="brand__name">Dunecrest</span></div>

  <p class="center teaser">CURIOUS<br>TO KNOW</p>
  <h1 class="center headline">WHAT’S<br>YOUR HOUSE<br>IS WORTH?</h1>

  <div class="cta">
    <p class="cta__label">CONTACT US TODAY</p>
    <p class="cta__phone">03 9012 4477</p>
  </div>
</section>

<section class="flyer flyer--back">
  <svg class="flyer__art" viewBox="0 0 437 920" aria-hidden="true">
    <defs>
      <linearGradient id="portraitTone" x1="0" y1="0" x2="0" y2="1">
        <stop offset="0" stop-color="#8d8d8d"/>
        <stop offset="1" stop-color="#b9b9b9"/>
      </linearGradient>
    </defs>
    <rect width="437" height="920" fill="var(--paper)"/>
    <polygon points="0,0 437,0 437,489 0,489" fill="var(--navy)"/>
    <path d="M32,534 L32,330 Q40,305 100,290 L150,270 L150,150 Q218,120 286,150 L286,270 L336,290 Q372,305 372,330 L372,534 Z" fill="url(#portraitTone)" role="img" aria-label="Black and white portrait of the managing director in a suit and tie"/>
    <polygon points="0,489 218,548 437,489 437,494 218,562 0,494" fill="var(--navy)"/>
    <polygon points="0,494 218,562 437,494 437,500 218,574 0,500" fill="var(--red)"/>
    <polygon points="0,500 218,574 437,500 437,920 0,920" fill="var(--paper)"/>
  </svg>

  <div class="brand"><span class="brand__mark"></span><span class="brand__name">Dunecrest</span></div>

  <h2 class="center agent__name">Arjun Malhotra</h2>
  <p class="center agent__role">Managing Director/LEA,<br>Dunecrest Real Estate</p>

  <svg class="agent__icons" viewBox="0 0 252 24" aria-hidden="true">
    <line x1="0" y1="12" x2="252" y2="12" stroke="var(--navy)" stroke-width="1"/>
    <circle cx="84" cy="12" r="11" fill="var(--red)" stroke="var(--navy)" stroke-width="1.5"/>
    <rect x="78" y="8" width="12" height="8" fill="none" stroke="var(--white)" stroke-width="1.3"/>
    <polyline points="78,8 84,13 90,8" fill="none" stroke="var(--white)" stroke-width="1.3"/>
    <circle cx="126" cy="12" r="11" fill="var(--red)" stroke="var(--navy)" stroke-width="1.5"/>
    <circle cx="126" cy="12" r="6" fill="none" stroke="var(--white)" stroke-width="1.3"/>
    <line x1="120" y1="12" x2="132" y2="12" stroke="var(--white)" stroke-width="1"/>
    <ellipse cx="126" cy="12" rx="2.5" ry="6" fill="none" stroke="var(--white)" stroke-width="1"/>
    <circle cx="165" cy="12" r="11" fill="var(--red)" stroke="var(--navy)" stroke-width="1.5"/>
    <path d="M165,19 C161,14 160,12 160,10 A5,5 0 0 1 170,10 C170,12 169,14 165,19 Z" fill="var(--white)"/>
    <circle cx="165" cy="10" r="1.8" fill="var(--red)"/>
  </svg>

  <p class="center agent__contact">arjun@dunecrestrealty.com.au<br>www.dunecrestrealty.com.au<br>14/8 Horizon Pde, Tarneit, VIC 3030</p>

  <div class="cta">
    <p class="cta__label">CONTACT US TODAY</p>
    <p class="cta__phone">03 9012 4477</p>
  </div>
</section>

<span class="side-label side-label--front">FRONT</span>
<span class="side-label side-label--back">BACK</span>
<p class="caption">Design Concept Dunecrest Real Estate DL Flyer 01</p>

</body>
</html>
```